Business Card for Professional Photographer

I'm looking for an eye catching modern clean design that compliments my logo/ website fonts & colours.
I specialise in architecture, corporate & commercial photography so I'm marketing to professional clients rather than portrait / wedding clients.

I would prefer to not have a solid black design.

My logo brand guide is as follows :

Main front font. : Reislust
Main font colour : #fff
Slogan front font : Ubuntu Bold
Monogram front font : Venti Medium
Container colour : #fff

I need print ready files in pdf .png & .eps formats.

Included in the files below are some screen grabs as reference to font & colours etc.

```html
<!DOCTYPE html>
<html lang="en">
<head>
<meta charset="utf-8">
<title>Clear Frame – Business Card</title>
<link rel="stylesheet" href="https://fonts.googleapis.com/css2?family=Josefin+Sans:wght@300;400;600&display=swap">
<style>
  :root {
    --backdrop: #e6e6e4;
    --card-dark: #0d0907;
    --card-glow: #2a1d17;
    --gold: #d9b872;
    --gold-light: #ecd39a;
    --gold-deep: #b8934c;
    --steel-dark: #1b1c1f;
    --steel-mid: #3a3d43;
    --steel-light: #8c9097;
    --text-gold: #d6b56e;
    --icon-ink: #1a1410;
  }
  * { margin: 0; padding: 0; box-sizing: border-box; }
  html, body { width: 1200px; height: 854px; overflow: hidden; }
  body {
    background: var(--backdrop);
    font-family: "Josefin Sans", sans-serif;
    position: relative;
  }
  .card {
    position: absolute;
    width: 560px;
    height: 320px;
    background: radial-gradient(ellipse at 55% 45%, var(--card-glow) 0%, #150e0b 55%, var(--card-dark) 100%);
    overflow: hidden;
    box-shadow: 0 6px 18px rgba(0,0,0,.18);
  }
  .card--front { left: 40px; top: 60px; }
  .card--back { left: 600px; top: 474px; }
  .card__texture {
    position: absolute; inset: 0;
  }
  .card__corners {
    position: absolute; inset: 0; width: 100%; height: 100%;
  }

  /* Front */
  .brand {
    position: absolute;
    left: 180px; top: 138px;
    display: flex; align-items: center; gap: 14px;
  }
  .brand__mark {
    width: 34px; height: 34px;
    border: 2px solid var(--text-gold);
  }
  .brand__name {
    color: var(--text-gold);
    font-weight: 400;
    font-size: 19px;
    letter-spacing: 2.5px;
    line-height: 1;
  }
  .brand__slogan {
    margin-top: 5px;
    color: var(--text-gold);
    font-weight: 300;
    font-size: 6.5px;
    letter-spacing: 1.6px;
  }

  /* Back */
  .identity {
    position: absolute;
    left: 40px; top: 168px;
    color: var(--text-gold);
  }
  .identity__name {
    font-size: 27px;
    font-weight: 400;
    letter-spacing: 4px;
    line-height: 1;
  }
  .identity__role {
    margin-top: 6px;
    margin-left: 12px;
    font-size: 10px;
    font-weight: 400;
    letter-spacing: 1.6px;
  }
  .contact {
    position: absolute;
    right: 52px; top: 82px;
    list-style: none;
    text-align: right;
    color: var(--text-gold);
    font-size: 11px;
    letter-spacing: 1.8px;
  }
  .contact li { height: 25px; line-height: 25px; }
  .contact__icons {
    position: absolute;
    right: 22px; top: 84px;
    display: flex; flex-direction: column; gap: 9px;
  }
  .contact__icon {
    width: 16px; height: 16px;
    background: var(--gold);
    border-radius: 2px;
    display: block;
  }
</style>
</head>
<body>

  <!-- Card front -->
  <section class="card card--front">
    <div class="card__texture" role="img" aria-label="Fine dark brown grid texture across the card surface"></div>
    <svg class="card__corners" viewBox="0 0 560 320" aria-hidden="true">
      <defs>
        <linearGradient id="goldFront" x1="0" y1="0" x2="1" y2="1">
          <stop offset="0" stop-color="#ecd39a"/>
          <stop offset="1" stop-color="#c9a35c"/>
        </linearGradient>
        <linearGradient id="steelFront" x1="0" y1="0" x2="1" y2="1">
          <stop offset="0" stop-color="#2a2c30"/>
          <stop offset="0.6" stop-color="#3f4248"/>
          <stop offset="1" stop-color="#1b1c1f"/>
        </linearGradient>
      </defs>
      <!-- top right -->
      <polygon points="455,0 560,0 560,88" fill="url(#goldFront)"/>
      <polygon points="445,0 455,0 560,88 560,98" fill="#5a4a36"/>
      <!-- bottom left -->
      <polygon points="0,180 0,272 250,320 330,320" fill="url(#steelFront)"/>
      <line x1="0" y1="180" x2="330" y2="320" stroke="#9a9ea5" stroke-width="2"/>
      <polygon points="0,262 0,320 145,320" fill="url(#goldFront)"/>
      <line x1="0" y1="262" x2="145" y2="320" stroke="#6b5436" stroke-width="1.5"/>
    </svg>
    <div class="brand">
      <span class="brand__mark"></span>
      <div>
        <div class="brand__name">CLEAR FRAME</div>
        <div class="brand__slogan">ARCHITECTURE · CORPORATE · COMMERCIAL</div>
      </div>
    </div>
  </section>

  <!-- Card back -->
  <section class="card card--back">
    <div class="card__texture" role="img" aria-label="Fine dark brown grid texture across the card surface"></div>
    <svg class="card__corners" viewBox="0 0 560 320" aria-hidden="true">
      <defs>
        <linearGradient id="goldBack" x1="0" y1="0" x2="1" y2="1">
          <stop offset="0" stop-color="#ecd39a"/>
          <stop offset="1" stop-color="#c9a35c"/>
        </linearGradient>
        <linearGradient id="steelBack" x1="0" y1="0" x2="1" y2="1">
          <stop offset="0" stop-color="#1b1c1f"/>
          <stop offset="0.5" stop-color="#3f4248"/>
          <stop offset="1" stop-color="#222427"/>
        </linearGradient>
      </defs>
      <!-- top right -->
      <polygon points="330,0 560,0 560,150" fill="url(#steelBack)"/>
      <line x1="330" y1="0" x2="560" y2="150" stroke="#9a9ea5" stroke-width="2"/>
      <polygon points="420,0 560,0 560,58" fill="url(#goldBack)"/>
      <line x1="420" y1="0" x2="560" y2="58" stroke="#6b5436" stroke-width="1.5"/>
      <!-- bottom left -->
      <polygon points="0,250 0,320 95,320" fill="url(#goldBack)"/>
      <line x1="0" y1="250" x2="95" y2="320" stroke="#6b5436" stroke-width="1.5"/>
    </svg>

    <div class="identity">
      <div class="identity__name">NAME TITLE</div>
      <div class="identity__role">DESIGNATION</div>
    </div>

    <ul class="contact">
      <li>000 000 0000</li>
      <li>000 000 0000</li>
      <li>WWW.SAMPLE.COM</li>
      <li>WWW.SAMPLE.COM</li>
      <li>SAMPLE@SAMPLE.COM</li>
    </ul>

    <div class="contact__icons">
      <svg class="contact__icon" viewBox="0 0 16 16" aria-label="Phone" role="img">
        <rect width="16" height="16" rx="2" fill="var(--gold)"/>
        <path d="M4 7c0-2 2-3 4-3s4 1 4 3l-2 .5-.5-1.5h-3L6 7.5z M5 12h6l-1-4H6z" fill="var(--icon-ink)"/>
      </svg>
      <svg class="contact__icon" viewBox="0 0 16 16" aria-label="Mobile" role="img">
        <rect width="16" height="16" rx="2" fill="var(--gold)"/>
        <rect x="5.5" y="3" width="5" height="10" rx="1" fill="none" stroke="var(--icon-ink)" stroke-width="1.2"/>
        <circle cx="8" cy="11.3" r=".6" fill="var(--icon-ink)"/>
      </svg>
      <svg class="contact__icon" viewBox="0 0 16 16" aria-label="Email" role="img">
        <rect width="16" height="16" rx="2" fill="var(--gold)"/>
        <rect x="3" y="4.5" width="10" height="7" fill="none" stroke="var(--icon-ink)" stroke-width="1.1"/>
        <path d="M3 4.5l5 4 5-4" fill="none" stroke="var(--icon-ink)" stroke-width="1.1"/>
      </svg>
      <svg class="contact__icon" viewBox="0 0 16 16" aria-label="Website" role="img">
        <rect width="16" height="16" rx="2" fill="var(--gold)"/>
        <circle cx="8" cy="8" r="4.5" fill="none" stroke="var(--icon-ink)" stroke-width="1.1"/>
        <ellipse cx="8" cy="8" rx="2" ry="4.5" fill="none" stroke="var(--icon-ink)" stroke-width=".9"/>
        <line x1="3.5" y1="8" x2="12.5" y2="8" stroke="var(--icon-ink)" stroke-width=".9"/>
      </svg>
    </div>
  </section>

</body>
</html>
```